KRV Business Card - Courier/Transportation - Needs Double Sided Business Card

I am searching for business cards for my company. Currently I just need cards for the (3) founders.

We are a new courier/transporation company that specializes in the medical/pharmaceutical arena.

As you will see from our logo, our primary colors are green and black. We strive to have an efficient, streamlined service offering. I like traditional looks, but also want to showcase our young, modern feel. I would like our card to be double sided.

Target Market(s)

Pharmacies
Hospitals
Physcian Office
Labs

Industry/Entity Type

Business

```html
<!DOCTYPE html>
<html lang="en">
<head>
<meta charset="utf-8">
<title>KRV Business Card</title>
<link rel="stylesheet" href="https://fonts.googleapis.com/css2?family=Michroma&family=Montserrat:wght@400;500;600&family=Merriweather:ital,wght@1,700&display=swap">
<style>
  :root {
    --bg: #2a2b2d;
    --card-white: #f7f7f5;
    --ink: #262626;
    --panel: #1f1d1d;
    --green: #27b340;
    --green-light: #3fcf55;
    --text-light: #f2f2f2;
  }
  * { box-sizing: border-box; margin: 0; padding: 0; }
  html, body { width: 1200px; height: 724px; overflow: hidden; }
  body {
    background: var(--bg);
    position: relative;
    font-family: "Montserrat", sans-serif;
  }
  .card {
    position: absolute;
    width: 540px;
    height: 310px;
    background: var(--card-white);
    overflow: hidden;
    box-shadow: 0 10px 28px rgba(0,0,0,0.45);
  }
  .card-front { left: 40px; top: 207px; }
  .card-back { left: 620px; top: 207px; }
  .card svg.shape { position: absolute; inset: 0; }

  .wordmark {
    position: absolute;
    display: flex;
    align-items: center;
    gap: 14px;
    font-family: "Montserrat", sans-serif;
    font-weight: 600;
    color: var(--ink);
    white-space: nowrap;
    line-height: 1;
  }
  .wordmark .mark-square { background: var(--green); }
  .card-front .wordmark { left: 50px; top: 98px; font-size: 76px; }
  .card-front .wordmark .mark-square { width: 40px; height: 40px; }
  .card-back .wordmark { left: 30px; top: 78px; font-size: 44px; }
  .card-back .wordmark .mark-square { width: 24px; height: 24px; }

  .front-url {
    position: absolute; left: 50px; top: 62px;
    font-family: "Michroma", sans-serif;
    font-size: 11px; color: var(--green); letter-spacing: 1px;
  }

  .address-band {
    position: absolute; left: 14px; top: 165px;
    width: 270px; height: 50px;
    background: var(--green);
    color: #fff;
    font-family: "Michroma", sans-serif;
    font-size: 9.5px; letter-spacing: 1px; line-height: 1.7;
    padding: 8px 0 0 18px;
  }

  .contact {
    position: absolute; right: 26px; color: var(--text-light); text-align: right;
  }
  .contact-name { top: 64px; font-size: 24px; font-weight: 500; }
  .contact-role {
    top: 96px; font-family: "Merriweather", serif; font-style: italic;
    font-weight: 700; font-size: 12px; color: var(--green);
  }
  .contact-line {
    display: flex; align-items: center; justify-content: flex-end; gap: 10px;
    font-size: 11px; letter-spacing: 1px;
  }
  .contact-phone { top: 150px; }
  .contact-email { top: 176px; }
  .contact-line svg { width: 16px; height: 14px; }
  .contact-web {
    top: 226px; font-family: "Michroma", sans-serif;
    font-size: 12.5px; color: var(--green); letter-spacing: 1.5px;
  }
</style>
</head>
<body>

  <section class="card card-front" aria-label="Card front">
    <svg class="shape" viewBox="0 0 540 310" aria-hidden="true">
      <polygon points="0,310 0,235 50,190 540,190 540,310" fill="var(--panel)"/>
      <polygon points="380,190 540,190 540,130 420,130" fill="var(--panel)"/>
    </svg>
    <p class="front-url">www.KRVtransit.net</p>
    <div class="wordmark"><span class="mark-square"></span>KRV</div>
  </section>

  <section class="card card-back" aria-label="Card back">
    <svg class="shape" viewBox="0 0 540 310" aria-hidden="true">
      <polygon points="300,48 540,48 540,310 264,310 300,262" fill="var(--panel)"/>
      <polygon points="300,48 330,28 330,38 470,38 470,48" fill="var(--green)"/>
      <polygon points="470,38 540,52 540,60 470,48" fill="var(--green-light)"/>
    </svg>
    <div class="wordmark"><span class="mark-square"></span>KRV</div>
    <div class="address-band">2847 Linden Ridge Dr,<br>Carmel, IN 46032</div>

    <p class="contact contact-name">Dana Reyes</p>
    <p class="contact contact-role">Founder</p>
    <p class="contact contact-line contact-phone">0455 318 204
      <svg viewBox="0 0 16 16" aria-hidden="true"><path d="M3 1l3 3-2 2c1 2 3 4 5 5l2-2 3 3-2 3C7 15 1 9 1 3z" fill="var(--green)"/></svg>
    </p>
    <p class="contact contact-line contact-email">dana.reyes@krvtransit.net
      <svg viewBox="0 0 16 14" aria-hidden="true"><rect x="0.5" y="1.5" width="15" height="11" fill="var(--green)"/><path d="M1 2l7 6 7-6" stroke="var(--panel)" stroke-width="1.2" fill="none"/></svg>
    </p>
    <p class="contact contact-web">www.KRVtransit.net</p>
  </section>

</body>
</html>
```